Zielgruppe
Das Buch 'Goldene Funken im stillen Alltag' Untertitel: Notizen und Skizzen vom Ufer bis zum Gipfel' ist eine Community-Projekt und versammelt die Texte von 22 Coach*innen unter einem Cover. Die Rat gebenden Texte und sinnreichen Geschichten handeln von Mut, Selbstliebe, innerer Weisheit, persönlicher Entwicklung und natürlich vom Leben. Die Zielgruppe sind Frauen von 35-55 Jahren mit Interesse an Spiritualität, persönlicher Weiterentwicklung und Inspirationen. Sie wollen ihr Leben (um)gestalten und suchen nach neuen Möglichkeiten. Sie mögen warme und weiche Farben eher als allzu Schrilles, doch eher Modernes als Altbackenes oder Verschnörkeltes.
Aufgabenstellung
Es wäre schön, wenn der Geschenk-Charakter aus dem Titel auch im Cover widergespiegelt würde.

```html
<!DOCTYPE html>
<html lang="de">
<head>
<meta charset="utf-8">
<title>Goldene Funken im stillen Alltag – Buchcover</title>
<link rel="stylesheet" href="https://fonts.googleapis.com/css2?family=Raleway:wght@800&family=Great+Vibes&family=Kaushan+Script&display=swap">
<style>
  :root {
    --paper: #ffffff;
    --paper-warm: #fff8dc;
    --ink-brown: #5b3d1f;
    --ribbon-gold: #e1b84a;
    --ribbon-light: #f0d27a;
    --ribbon-dark: #c99a2e;
    --bow-gold: #e3bd52;
    --tag-gold: #e6cf7c;
    --tag-light: #f3e3a6;
    --tag-dark: #cfb257;
  }
  html, body {
    margin: 0;
    padding: 0;
    width: 750px;
    height: 1200px;
    overflow: hidden;
    background: var(--paper);
  }
  .cover {
    position: relative;
    width: 750px;
    height: 1200px;
    overflow: hidden;
    background: var(--paper);
  }
  .sparkle-field {
    position: absolute;
    inset: 0;
    background:
      radial-gradient(ellipse at 75% 20%, var(--paper-warm) 0%, transparent 45%),
      radial-gradient(ellipse at 20% 75%, var(--paper-warm) 0%, transparent 45%),
      radial-gradient(ellipse at 80% 80%, #fffbe9 0%, transparent 40%);
  }
  .ribbon-art {
    position: absolute;
    inset: 0;
    width: 750px;
    height: 1200px;
  }
  .title-block {
    position: absolute;
    left: 284px;
    top: 446px;
    width: 421px;
    height: 291px;
    border-top: 1.5px solid var(--ink-brown);
    border-bottom: 1.5px solid var(--ink-brown);
    color: var(--ink-brown);
    text-align: right;
  }
  .title-top {
    position: absolute;
    right: 0;
    top: 20px;
    margin: 0;
    font-family: "Raleway", sans-serif;
    font-weight: 800;
    font-size: 57px;
    letter-spacing: -0.5px;
    line-height: 1;
  }
  .title-script {
    position: absolute;
    right: 4px;
    top: 62px;
    margin: 0;
    font-family: "Great Vibes", cursive;
    font-weight: 400;
    font-size: 138px;
    line-height: 1.1;
  }
  .title-bottom {
    position: absolute;
    right: 0;
    top: 232px;
    margin: 0;
    font-family: "Raleway", sans-serif;
    font-weight: 800;
    font-size: 41px;
    letter-spacing: -0.3px;
    line-height: 1;
  }
  .subtitle-tag {
    position: absolute;
    inset: 0;
    width: 750px;
    height: 1200px;
  }
  .subtitle-text {
    position: absolute;
    left: 285px;
    top: 888px;
    width: 450px;
    margin: 0;
    transform: rotate(-10deg);
    transform-origin: center;
    font-family: "Kaushan Script", cursive;
    font-size: 47px;
    line-height: 68px;
    color: var(--ink-brown);
    text-align: center;
  }
</style>
</head>
<body>
<main class="cover">
  <div class="sparkle-field" role="img" aria-label="Goldene Funken und Lichtpunkte über dem weißen Grund"></div>

  <svg class="ribbon-art" viewBox="0 0 750 1200">
    <defs>
      <linearGradient id="band-vertical" x1="0" x2="1" y1="0" y2="0">
        <stop offset="0" stop-color="var(--ribbon-dark)"/>
        <stop offset="0.5" stop-color="var(--ribbon-gold)"/>
        <stop offset="1" stop-color="var(--ribbon-dark)"/>
      </linearGradient>
      <linearGradient id="band-horizontal" x1="0" x2="0" y1="0" y2="1">
        <stop offset="0" stop-color="var(--ribbon-gold)"/>
        <stop offset="0.5" stop-color="var(--ribbon-light)"/>
        <stop offset="1" stop-color="var(--ribbon-gold)"/>
      </linearGradient>
      <radialGradient id="bow-area" cx="0.45" cy="0.45" r="0.55">
        <stop offset="0" stop-color="var(--ribbon-light)"/>
        <stop offset="0.55" stop-color="var(--bow-gold)"/>
        <stop offset="0.85" stop-color="var(--bow-gold)" stop-opacity="0.5"/>
        <stop offset="1" stop-color="var(--bow-gold)" stop-opacity="0"/>
      </radialGradient>
    </defs>
    <rect class="ribbon-vertical" x="113" y="0" width="120" height="1200" fill="url(#band-vertical)"/>
    <polygon class="ribbon-horizontal" points="0,212 750,206 750,314 0,318" fill="url(#band-horizontal)"/>
    <ellipse class="bow-area" cx="190" cy="300" rx="260" ry="300" fill="url(#bow-area)" role="img" aria-label="Große goldene Satinschleife, die das Band wie bei einem Geschenk zusammenhält"/>
  </svg>

  <header class="title-block">
    <h1 class="title-top">GOLDENE</h1>
    <p class="title-script">Funken</p>
    <p class="title-bottom">IM STILLEN ALLTAG</p>
  </header>

  <svg class="subtitle-tag" viewBox="0 0 750 1200" aria-hidden="true">
    <defs>
      <linearGradient id="tag-fill" x1="0" x2="1" y1="0" y2="1">
        <stop offset="0" stop-color="var(--tag-light)"/>
        <stop offset="0.5" stop-color="var(--tag-gold)"/>
        <stop offset="1" stop-color="var(--tag-dark)"/>
      </linearGradient>
    </defs>
    <polygon points="296,908 704,840 714,838 737,856 749,1096 736,1116 330,1158 318,1144 286,960 280,930" fill="url(#tag-fill)"/>
  </svg>
  <p class="subtitle-text">Notizen und Skizzen<br>vom Ufer bis<br>zum Gipfel</p>
</main>
</body>
</html>
```